Beacon Lending and Capital. We provide MOSTLY residential home mortgages in Florida AND commercial loans for investment properties throughout the United states.
I would love to emulate so of the lender sites that are available on the internet but I would like to have the site as popular as possible for SEO purposes. Clients can already click the link to take them to the mortgage application where they can complete that and upload documents. If you could polish that up for me that would be great. I can also provide you with great detail on loan programs that are currently being offered. WE OFFER ALL MORTGAGE LENDING PRODUCTS. I would also like to add something in reference to the rate but I don't think it's legal to actually state or promise a rate for mortgage since they vary based on loan type, client and other criteria...

On the Beacon real estate site I would like to add a link or some way for clients to be able to put in credit card information to render services ...

Please let me know what you need from me

Thank you !!

Current link to site to improve and code

https://beaconlendingandcapital.example/

Industry/Entity Type

Residential and commmercial lending

Coding

Coded - Design and coding required

Number of Pages Required

2 page

Requirements
Must have
• Love to integrate Mortgage interest rates even if general
Nice to have
• Link to fill out mortgage application via Quillo MLO software

```html
<!DOCTYPE html>
<html lang="en">
<head>
<meta charset="utf-8">
<title>Beacon Lending and Capital of Florida</title>
<link href="https://fonts.googleapis.com/css2?family=Poppins:wght@400;500;600;700;800&family=Roboto+Condensed:wght@400;500&display=swap" rel="stylesheet">
<style>
:root{
  --green:#8dbb3f;
  --green-bright:#9cc33f;
  --forest:#1f3a1b;
  --forest-deep:#1a3d1c;
  --ink:#1d2a1a;
  --text:#222;
  --muted:#8a8a8a;
  --line:#d6d6d6;
  --white:#fff;
}
*{box-sizing:border-box;margin:0;padding:0}
html,body{width:1200px;height:2926px;overflow:hidden}
body{position:relative;font-family:'Poppins',sans-serif;color:var(--text);background:var(--white)}
.abs{position:absolute}

/* header */
.site-header{position:absolute;left:0;top:0;width:1200px;height:118px;background:var(--white);border-top:3px solid var(--green)}
.brand{position:absolute;display:flex;align-items:center;gap:14px}
.brand-mark{width:64px;height:64px;border-radius:50%;background:var(--forest)}
.brand-name{font-weight:600;color:var(--forest);line-height:1}
.brand-name .n1{display:block;font-size:13.5px;letter-spacing:.6px}
.brand-name .n2{display:block;font-size:11px;letter-spacing:5.2px;margin-top:9px}
.nav a{position:absolute;font-size:15px;color:var(--ink);text-decoration:none}
.nav .active{left:632px;top:0;width:62px;height:115px;background:linear-gradient(#eee,#f7f7f7);border-bottom:4px solid var(--green);padding-top:47px;text-align:center;font-weight:500}
.btn-pill{display:flex;align-items:center;justify-content:space-between;background:var(--green);color:var(--white);border-radius:22px;font-weight:500}
.arrow-dot{width:15px;height:15px;border-radius:50%;background:var(--white);display:inline-flex;align-items:center;justify-content:center}

/* hero */
.hero{position:absolute;left:0;top:118px;width:1200px;height:557px;background:linear-gradient(180deg,#0f7e92 0%,#3b6d6e 30%,#a2683a 62%,#5d3a1c 82%,#2d2413 100%)}
.hero-photo{position:absolute;inset:0;background:radial-gradient(ellipse at 58% 60%,rgba(220,140,60,.55),rgba(0,0,0,0) 55%),linear-gradient(90deg,rgba(0,0,0,.35),rgba(0,0,0,0) 60%)}
.hero-sub{position:absolute;left:85px;top:115px;font-family:'Roboto Condensed',sans-serif;font-size:16px;color:var(--white)}
.hero-title{position:absolute;left:85px;top:155px;font-size:40px;line-height:45.5px;font-weight:800;color:var(--white);text-transform:uppercase}
.hero-title .hl{color:var(--green-bright)}
.hero-cta{position:absolute;left:85px;top:357px;width:438px;height:38px;padding:0 14px 0 16px;font-size:16px;white-space:nowrap;overflow:hidden}

.quote{position:absolute;left:717px;top:206px;width:396px;height:376px;background:var(--green);border-radius:12px;overflow:hidden}
.quote-head{height:60px;background:var(--forest);color:var(--white);font-size:35px;font-weight:700;padding:10px 0 0 26px;border-radius:12px 12px 0 0}
.field{position:absolute;height:28px;background:var(--white);border-radius:3px;font-size:11px;color:#333;padding:7px 8px;display:flex;justify-content:space-between}
.field .caret{font-size:8px}
.quote-btn{position:absolute;left:23px;top:320px;width:351px;height:32px;background:var(--forest);color:var(--white);border-radius:3px;text-align:center;font-weight:700;font-size:15px;line-height:32px}

/* section headings */
.sec-mark{position:absolute;border-radius:50%;background:var(--forest)}
.sec-title{position:absolute;left:0;width:1200px;text-align:center;font-size:40px;font-weight:700;color:var(--forest);text-transform:uppercase}
.sec-title .hl{color:var(--green-bright)}

/* properties */
.card{position:absolute;top:920px;width:313px;height:582px;background:var(--white);box-shadow:0 0 10px rgba(0,0,0,.12)}
.card-photo{position:absolute;left:9px;top:9px;width:296px;height:445px}
.card h3{position:absolute;left:22px;top:478px;font-size:19px;font-weight:600;color:var(--forest)}
.card p{position:absolute;left:22px;top:516px;width:260px;font-size:12px;line-height:20px;color:#222}
.card-go{position:absolute;left:258px;top:473px;width:39px;height:39px;border-radius:50%;background:var(--green-bright);display:flex;align-items:center;justify-content:center}
.dots span{position:absolute;top:1558px;width:34px;height:4px;background:var(--forest)}

/* calculator */
.calc-label{position:absolute;width:200px;text-align:right;left:571px;font-size:18px;color:#333}
.calc-input{position:absolute;left:801px;width:311px;height:42px;border:1px solid #bbb;border-radius:4px;display:flex;align-items:center;padding:0 14px;font-size:18px;color:#222;gap:12px}
.calc-input .ico{color:var(--green);font-weight:600;font-size:16px}
.calc-input .caret{margin-left:auto;font-size:13px}
.calc-btn{position:absolute;left:801px;top:2000px;width:311px;height:41px;border-radius:4px;padding:0 16px 0 24px;font-size:18px;font-weight:600}

/* contact */
.contact{position:absolute;left:0;top:2137px;width:1200px;height:664px;background:linear-gradient(180deg,#1f4a1e 0%,#264f24 60%,#2c5727 100%)}
.contact-sub{position:absolute;left:0;width:1200px;top:212px;text-align:center;color:var(--white);font-size:15px}
.c-field{position:absolute;background:var(--white);border:1px solid #ccc;font-size:15px;color:var(--muted);padding:0 14px;display:flex;align-items:center}
.send{position:absolute;left:252px;top:554px;width:695px;height:53px;background:var(--green-bright);color:var(--white);font-weight:600;text-align:center;line-height:53px;font-size:16px}

/* footer */
.site-footer{position:absolute;left:0;top:2801px;width:1200px;height:125px;background:var(--white)}
.copy{position:absolute;left:772px;top:47px;font-size:14px;color:#222}
.social{position:absolute;top:39px;width:28px;height:28px;border-radius:50%;background:var(--green-bright)}
</style>
</head>
<body>

<header class="site-header">
  <div class="brand" style="left:85px;top:22px">
    <div class="brand-mark"></div>
    <div class="brand-name"><span class="n1">BEACON LENDING AND CAPITAL OF FLORIDA</span><span class="n2">BUSINESS AND COMMERCIAL DIVISION</span></div>
  </div>
  <nav class="nav">
    <a class="active" href="#">Home</a>
    <a href="#" style="left:726px;top:47px">About</a>
    <a href="#" style="left:810px;top:47px">Properties</a>
  </nav>
  <a class="btn-pill" href="#" style="position:absolute;left:925px;top:37px;width:189px;height:39px;padding:0 12px 0 16px;font-size:15.5px;text-decoration:none">Get a quick Quote
    <span class="arrow-dot"><svg width="9" height="9" viewBox="0 0 10 10"><path d="M2 5h6M5 2l3 3-3 3" stroke="#8dbb3f" stroke-width="1.8" fill="none"/></svg></span></a>
</header>

<section class="hero">
  <div class="hero-photo" role="img" aria-label="Aerial view of a Florida city skyline with high-rise towers along a river at sunset"></div>
  <p class="hero-sub">Residential home loans in florida &amp; commercial lending in america</p>
  <h1 class="hero-title">Your best resource<br>for hassle-free,<br><span class="hl">low cost mortgage</span><br>origination</h1>
  <a class="btn-pill hero-cta" href="#" style="text-decoration:none">Fill out mortgage application to begin lending pr
    <span class="arrow-dot" style="flex:none;margin-left:12px"><svg width="9" height="9" viewBox="0 0 10 10"><path d="M2 5h6M5 2l3 3-3 3" stroke="#8dbb3f" stroke-width="1.8" fill="none"/></svg></span></a>

  <form class="quote" style="top:88px">
    <div class="quote-head">GET A QUICK QUOTE</div>
    <div class="field" style="left:23px;top:76px;width:169px">Type of Loan<span class="caret">▼</span></div>
    <div class="field" style="left:203px;top:76px;width:171px">Rate Your Credit<span class="caret">▼</span></div>
    <div class="field" style="left:23px;top:125px;width:169px">Loan Amount<span class="caret">▼</span></div>
    <div class="field" style="left:203px;top:125px;width:171px">Property Value<span class="caret">▼</span></div>
    <div class="field" style="left:23px;top:173px;width:169px">State<span class="caret">▼</span></div>
    <div class="field" style="left:203px;top:173px;width:171px">Zip Code</div>
    <div class="field" style="left:23px;top:222px;width:169px">First Name</div>
    <div class="field" style="left:203px;top:222px;width:171px">Last Name</div>
    <div class="field" style="left:23px;top:271px;width:169px">Email</div>
    <div class="field" style="left:203px;top:271px;width:171px">Phone</div>
    <div class="quote-btn">GET MY QUOTE</div>
  </form>
</section>

<!-- properties -->
<div class="sec-mark" style="left:569px;top:736px;width:62px;height:62px"></div>
<h2 class="sec-title" style="top:824px"><span class="hl">Available</span> Properties</h2>

<article class="card" style="left:41px">
  <div class="card-photo" role="img" aria-label="Modern white and grey townhouse with balcony" style="background:linear-gradient(160deg,#9fc3df 0%,#e6e6e6 35%,#8c8c8c 70%,#3c3c3c 100%)"></div>
  <h3>12 Sunset Street</h3>
  <span class="card-go"><svg width="16" height="16" viewBox="0 0 16 16"><path d="M4 12L12 4M6 4h6v6" stroke="#fff" stroke-width="1.6" fill="none"/></svg></span>
  <p>Lorem Ipsum is simply dummy text of the printing and typesetting industry.</p>
</article>
<article class="card" style="left:384px">
  <div class="card-photo" role="img" aria-label="Dark modern house with wood slat entrance lit at dusk" style="background:linear-gradient(160deg,#2a3a2a 0%,#1d2530 45%,#5b4630 75%,#b0763a 100%)"></div>
  <h3>34 Union Avenue</h3>
  <span class="card-go"><svg width="16" height="16" viewBox="0 0 16 16"><path d="M4 12L12 4M6 4h6v6" stroke="#fff" stroke-width="1.6" fill="none"/></svg></span>
  <p>Lorem Ipsum is simply dummy text of the printing and typesetting industry.</p>
</article>
<article class="card" style="left:727px">
  <div class="card-photo" role="img" aria-label="Contemporary house with perforated facade beside a swimming pool" style="background:linear-gradient(170deg,#7fa6cc 0%,#c9d6e0 35%,#b59a78 62%,#3fb6d6 85%,#1e98c4 100%)"></div>
  <h3>56 Washington Street</h3>
  <span class="card-go"><svg width="16" height="16" viewBox="0 0 16 16"><path d="M4 12L12 4M6 4h6v6" stroke="#fff" stroke-width="1.6" fill="none"/></svg></span>
  <p>Lorem Ipsum is simply dummy text of the printing and typesetting industry.</p>
</article>
<article class="card" style="left:1066px">
  <div class="card-photo" role="img" aria-label="Modern house with red cladding and dark panels" style="background:linear-gradient(170deg,#8a4a3a 0%,#4d5a66 45%,#2a3038 100%)"></div>
  <h3 style="white-space:nowrap">78 Oak Boulevard</h3>
  <p>Lorem Ipsum is simply dummy text of the printing and typesetting industry.</p>
</article>

<div class="dots">
  <span style="left:479px"></span>
  <span style="left:531px;background:var(--green-bright)"></span>
  <span style="left:582px"></span>
  <span style="left:634px"></span>
  <span style="left:685px"></span>
</div>

<!-- calculator -->
<svg class="abs" style="left:80px;top:1620px" width="460" height="460" viewBox="0 0 460 460">
  <circle cx="227" cy="226" r="220" fill="none" stroke="#ddd" stroke-width="2"/>
  <path d="M85 366 A195 195 0 0 1 380 106" fill="none" stroke="#9cc33f" stroke-width="10"/>
</svg>
<div class="abs" role="img" aria-label="Person holding a smartphone with glowing house and percentage icons" style="left:129px;top:1668px;width:356px;height:356px;border-radius:50%;background:radial-gradient(circle at 55% 55%,#3b4a3c 0%,#1c231c 70%)"></div>
<div class="abs" style="left:456px;top:1840px;width:136px;height:136px;border-radius:50%;background:var(--forest)"></div>

<div class="sec-mark" style="left:830px;top:1646px;width:62px;height:62px"></div>
<h2 class="abs" style="left:608px;top:1735px;font-size:40px;font-weight:700;color:var(--forest)"><span style="color:var(--green-bright)">MORTGAGE</span> CALCULATIOR</h2>

<label class="calc-label" style="top:1834px">Mortgage Amount</label>
<div class="calc-input" style="top:1829px"><span class="ico">$</span>250,000</div>
<label class="calc-label" style="top:1890px">Mortgage Term</label>
<div class="calc-input" style="top:1884px"><span class="ico">
  <svg width="13" height="13" viewBox="0 0 13 13"><rect x="1" y="2" width="11" height="10" fill="none" stroke="#8dbb3f" stroke-width="1.4"/><path d="M1 5h11M4 1v2M9 1v2" stroke="#8dbb3f" stroke-width="1.4"/></svg></span>30 Years<span class="caret">▼</span></div>
<label class="calc-label" style="top:1944px">Interest Rate</label>
<div class="calc-input" style="top:1938px"><span class="ico">%</span>4.125<span class="caret">▼</span></div>
<div class="btn-pill calc-btn">CALCULATE NOW
  <span class="arrow-dot"><svg width="9" height="9" viewBox="0 0 10 10"><path d="M2 5h6M5 2l3 3-3 3" stroke="#8dbb3f" stroke-width="1.8" fill="none"/></svg></span></div>

<!-- contact -->
<section class="contact">
  <div role="img" aria-label="Faint city skyline tinted green" style="position:absolute;left:0;top:340px;width:1200px;height:324px;background:linear-gradient(180deg,rgba(60,100,50,0),rgba(70,110,55,.35))"></div>
  <div class="sec-mark" style="left:569px;top:56px;width:62px;height:62px;background:var(--white)"></div>
  <h2 class="sec-title" style="top:147px;color:var(--white)">Get in <span class="hl">Touch</span></h2>
  <p class="contact-sub">Please send me a message for general inquiries or reservations.</p>
  <div class="c-field" style="left:252px;top:254px;width:342px;height:52px">FIRST NAME*</div>
  <div class="c-field" style="left:605px;top:254px;width:342px;height:52px">LAST NAME*</div>
  <div class="c-field" style="left:252px;top:319px;width:342px;height:52px">E-MAIL*</div>
  <div class="c-field" style="left:605px;top:319px;width:342px;height:52px">PHONE*</div>
  <div class="c-field" style="left:252px;top:384px;width:695px;height:157px;align-items:flex-start;padding-top:18px">MESSAGE</div>
  <div class="send">SEND NOW</div>
</section>

<footer class="site-footer">
  <div class="brand" style="left:85px;top:22px">
    <div class="brand-mark"></div>
    <div class="brand-name"><span class="n1">BEACON LENDING AND CAPITAL OF FLORIDA</span><span class="n2">BUSINESS AND COMMERCIAL DIVISION</span></div>
  </div>
  <p class="copy">© 2025. All Rights Reserved.</p>
  <span class="social" style="left:1004px"></span>
  <span class="social" style="left:1045px"></span>
  <span class="social" style="left:1085px"></span>
</footer>

</body>
</html>
```